BRIARFELL Real Estate
Real Estate Developer
Project: BRIARFELL Real Estate
BRIARFELL Real Estate - Real Estate
Creative Brief
Use specific fonts
Up to the designer!
Professional
Matthias L. Halvik
Managing Director
BRIARFELL Real Estate GmbH & Co. KG Lindauer Gang 14 20417 Hamburg Germany
mlh@briarfellre.com
briarfellre.com
One-sided or two-sided cards are welcome and any of the three logos and its colour variations can be chosen!

```html
<!DOCTYPE html>
<html lang="de">
<head>
<meta charset="utf-8">
<title>BRIARFELL Real Estate – Business Card</title>
<link href="https://fonts.googleapis.com/css2?family=Open+Sans:wght@400;600;700;800&display=swap" rel="stylesheet">
<style>
  :root{
    --stage:#d9d9d9;
    --card-white:#ffffff;
    --green:#2f5a36;
    --green-deep:#284d2e;
    --green-faint:rgba(255,255,255,0.09);
    --grey-band:#5b5b5b;
    --text-dark:#333333;
    --text-muted:#5a5a5a;
    --white:#ffffff;
  }
  *{box-sizing:border-box;margin:0;padding:0}
  html,body{width:1200px;height:842px;overflow:hidden}
  body{
    background:var(--stage);
    font-family:"Open Sans",Arial,sans-serif;
    position:relative;
  }
  .card{
    position:absolute;
    top:266px;
    width:540px;
    height:310px;
    box-shadow:0 6px 18px rgba(0,0,0,0.18);
    overflow:hidden;
  }
  /* ---------- front ---------- */
  .card-front{left:45px;background:var(--card-white)}
  .brand{
    position:absolute;top:46px;left:178px;
    display:flex;align-items:center;gap:12px;
  }
  .brand-dot{width:40px;height:40px;border-radius:50%;background:var(--green)}
  .brand-name{
    font-weight:800;font-size:31px;letter-spacing:1px;color:var(--green);
  }
  .name-band{
    position:absolute;left:0;top:136px;width:238px;height:44px;
    background:var(--grey-band);color:var(--white);
    padding:5px 0 0 24px;
  }
  .person-name{font-weight:700;font-size:12.5px;line-height:17px}
  .person-role{font-size:10px;line-height:14px;opacity:.9}
  .address{
    position:absolute;left:24px;top:196px;width:200px;
    font-size:9.5px;line-height:15px;color:var(--text-muted);
  }
  .contact-panel{
    position:absolute;left:238px;top:180px;width:302px;height:104px;
    background:var(--green);
    padding:12px 0 0 26px;
  }
  .contact-list{list-style:none}
  .contact-list li{
    display:flex;align-items:center;gap:8px;
    color:var(--white);font-size:10px;line-height:16px;
  }
  .contact-list svg{width:11px;height:11px;flex:none}
  /* ---------- back ---------- */
  .card-back{left:615px;background:var(--green-deep)}
  .back-circle{
    position:absolute;left:150px;top:34px;width:160px;height:160px;
    border-radius:50%;background:var(--green-faint);
  }
  .back-web{
    position:absolute;right:30px;bottom:34px;
    font-size:13px;letter-spacing:1.5px;color:rgba(255,255,255,0.28);
  }
</style>
</head>
<body>

<section class="card card-front" aria-label="Card front">
  <div class="brand">
    <span class="brand-dot"></span>
    <span class="brand-name">BRIARFELL</span>
  </div>

  <div class="name-band">
    <p class="person-name">Matthias L. Halvik</p>
    <p class="person-role">Managing Director</p>
  </div>

  <p class="address">
    BRIARFELL Real Estate GmbH &amp; Co. KG<br>
    Lindauer Gang 14 20417 Hamburg Germany
  </p>

  <div class="contact-panel">
    <ul class="contact-list">
      <li>
        <svg viewBox="0 0 12 12"><circle cx="6" cy="6" r="6" fill="#fff"/><path d="M4 3.2l1 1.4-.6.8c.4.8 1 1.4 1.8 1.8l.8-.6 1.4 1-.5 1.2C5.6 8.7 3.3 6.4 3 3.7z" fill="#2f5a36"/></svg>
        +49 (040) 5550184
      </li>
      <li>
        <svg viewBox="0 0 12 12"><circle cx="6" cy="6" r="6" fill="#fff"/><rect x="4.2" y="2.6" width="3.6" height="6.8" rx=".6" fill="#2f5a36"/></svg>
        +49 (0175) 5550327
      </li>
      <li>
        <svg viewBox="0 0 12 12"><circle cx="6" cy="6" r="6" fill="#fff"/><rect x="3" y="5" width="6" height="4" fill="#2f5a36"/><rect x="4" y="2.8" width="4" height="2.4" fill="#2f5a36"/></svg>
        +49 (040) 5550185
      </li>
      <li>
        <svg viewBox="0 0 12 12"><circle cx="6" cy="6" r="6" fill="#fff"/><rect x="3" y="4" width="6" height="4.2" fill="#2f5a36"/><path d="M3 4l3 2.4L9 4" stroke="#fff" stroke-width=".7" fill="none"/></svg>
        mlh@briarfellre.com
      </li>
      <li>
        <svg viewBox="0 0 12 12"><circle cx="6" cy="6" r="6" fill="#fff"/><circle cx="6" cy="6" r="3" fill="none" stroke="#2f5a36" stroke-width=".8"/><path d="M3 6h6M6 3v6" stroke="#2f5a36" stroke-width=".7"/></svg>
        www.briarfellre.com
      </li>
    </ul>
  </div>
</section>

<section class="card card-back" aria-label="Card back">
  <span class="back-circle"></span>
  <p class="back-web">www.briarfellre.com</p>
</section>

</body>
</html>
```